Redesign of business card for Silverbrook Mechanical

We are looking for a new design for our business cards for Silverbrook Mechanical. We are a plumbing & HVAC construction company, operating on the West Coast of Canada and USA. Logo attached.
Industry/Entity Type
Construction - Plumbing & HVAC
Contact Information for Business Card
Name, address, phone numbers, email, website address
Look and feel

```html
<!DOCTYPE html>
<html lang="en">
<head>
<meta charset="UTF-8">
<title>Silverbrook Mechanical – Business Card</title>
<link href="https://fonts.googleapis.com/css2?family=Poppins:wght@400;600&display=swap" rel="stylesheet">
<style>
  :root {
    --stage: #2b2b2d;
    --card: #0b0b0b;
    --ink: #ffffff;
    --silver: #c9c9c9;
    --rule: #8a8a8a;
  }
  * { margin: 0; padding: 0; box-sizing: border-box; }
  html, body { width: 1200px; height: 900px; overflow: hidden; }
  body {
    background: var(--stage);
    font-family: "Poppins", sans-serif;
    color: var(--ink);
    position: relative;
  }
  .card {
    position: absolute;
    width: 540px;
    height: 310px;
    background: var(--card);
    border-radius: 22px;
  }
  .card--front { left: 50px; top: 330px; }
  .card--back { left: 610px; top: 260px; }

  .brand {
    position: absolute;
    left: 34px;
    top: 0;
    height: 100%;
    width: 232px;
    display: flex;
    align-items: center;
    gap: 10px;
  }
  .brand__mark {
    width: 16px;
    height: 16px;
    background: var(--ink);
    flex: none;
  }
  .brand__name {
    font-weight: 600;
    font-size: 19px;
    line-height: 1.2;
    text-transform: uppercase;
    letter-spacing: 0.5px;
  }
  .divider {
    position: absolute;
    left: 280px;
    top: 62px;
    width: 1px;
    height: 190px;
    background: var(--rule);
  }
  .contact {
    position: absolute;
    left: 304px;
    top: 56px;
    right: 20px;
  }
  .contact__name {
    font-weight: 600;
    font-size: 20px;
    letter-spacing: 0.5px;
    line-height: 1.1;
    text-transform: uppercase;
  }
  .contact__role {
    font-size: 14px;
    margin-bottom: 14px;
  }
  .contact__list { list-style: none; }
  .contact__item {
    display: flex;
    align-items: center;
    gap: 6px;
    font-size: 13px;
    line-height: 22px;
    white-space: nowrap;
  }
  .contact__item svg { width: 13px; height: 13px; flex: none; }
  .contact__address {
    margin-top: 14px;
    font-size: 13px;
    line-height: 19px;
  }

  .card--back .brand--large {
    position: absolute;
    inset: 0;
    display: flex;
    align-items: center;
    justify-content: center;
    gap: 14px;
  }
  .brand--large .brand__mark {
    width: 22px;
    height: 22px;
    background: var(--silver);
  }
  .brand--large .brand__name {
    font-size: 28px;
    color: var(--silver);
  }
</style>
</head>
<body>

  <section class="card card--back" aria-label="Business card back">
    <div class="brand--large">
      <span class="brand__mark"></span>
      <span class="brand__name">Silverbrook Mechanical</span>
    </div>
  </section>

  <section class="card card--front" aria-label="Business card front">
    <div class="brand">
      <span class="brand__mark"></span>
      <span class="brand__name">Silverbrook<br>Mechanical</span>
    </div>

    <div class="divider"></div>

    <div class="contact">
      <p class="contact__name">Daniel Harper</p>
      <p class="contact__role">Managing Director</p>
      <ul class="contact__list">
        <li class="contact__item">
          <svg viewBox="0 0 24 24" fill="none" stroke="currentColor" stroke-width="2.2" stroke-linecap="round" stroke-linejoin="round"><path d="M5 3h4l2 5-2.5 1.5a11 11 0 0 0 6 6L16 13l5 2v4a2 2 0 0 1-2 2A16 16 0 0 1 3 5a2 2 0 0 1 2-2z"/></svg>
          044-555 014 273
        </li>
        <li class="contact__item">
          <svg viewBox="0 0 24 24" fill="none" stroke="currentColor" stroke-width="2.2" stroke-linejoin="round"><rect x="2" y="5" width="20" height="14" rx="1"/><path d="M2 6l10 7 10-7"/></svg>
          info@silverbrookmech.com
        </li>
        <li class="contact__item">
          <svg viewBox="0 0 24 24" fill="none" stroke="currentColor" stroke-width="2"><circle cx="12" cy="12" r="10"/><path d="M2 12h20M12 2c3 3 3 17 0 20M12 2c-3 3-3 17 0 20"/></svg>
          www.silverbrookmech.com
        </li>
      </ul>
      <p class="contact__address">421, Address line goes here<br>45452, Country Name</p>
    </div>
  </section>

</body>
</html>
```